International Life Insurer Needs a Web Design

What We Do: We are a boutique financial services firm specializing in solutions that financial services professionals can integrate into comprehensive wealth preservation strategies for their clients. Strategies we provide may run the spectrum from simple life insurance products to complex cases with very sophisticated and intricate solutions.

Industry Type: Financial & Insurance

Top Things to Communicate Through Our Web Design:
#1 Ultra High Net Worth
#2 INTERNATIONAL
#3 Private Banking
#4 Expertise
________________________________________
Our Target Audience:
Financial institutions/private banks who have high net worth/ultra high net worth international clients looking for unparalleled expertise in wealth preservation, taxation, and business insurance. The audience is the financial service professional, not the end client of the financial services. We will direct the professional to the site.
We Like These Designs. (fonts, colors, style):
Simple font, clean, modern, contemporary, blue colors
NOT stodgy, old, gothic, etc.

Secondarily, we’d like to also create a small tri-fold brochure incorporating the web elements (design, text), so the ability to transfer the design to print might be a plus.
Updates

Target Market(s)

Financial services professionals catering to their ultra high net worth clients

Industry/Entity Type

Life Insurance

Requirements
Must have
• Our logo (see uploaded file)
Nice to have
• the existing website includes some text that could be reviewed for ideas and incorporated into the design: http://harborlinecoveragepartners.example/

```html
<!DOCTYPE html>
<html lang="en">
<head>
<meta charset="utf-8">
<title>Harborline Coverage Partners</title>
<link href="https://fonts.googleapis.com/css2?family=Open+Sans:wght@400;600&display=swap" rel="stylesheet">
<style>
:root{
  --navy:#0a3a5e;
  --footer:#08375a;
  --text:#2b3f52;
  --heading:#1d2b38;
  --link:#3aa0ec;
  --white:#ffffff;
  --panel-border:#d3d8dd;
  --divider:#2e7fc4;
}
*{margin:0;padding:0;box-sizing:border-box}
html,body{width:1200px;height:2408px;overflow:hidden;background:var(--white)}
body{position:relative;font-family:"Open Sans",Arial,sans-serif;color:var(--text)}
.abs{position:absolute}

.brand{left:110px;top:66px;display:flex;align-items:center;gap:14px}
.brand-mark{width:98px;height:106px;background:var(--navy)}
.brand-name{font-size:34px;line-height:40px;color:var(--navy);white-space:nowrap}

.search{left:830px;top:108px;width:260px;height:54px;border:2px solid #c9cdd1;border-radius:4px;
  display:flex;align-items:center;justify-content:space-between;padding:0 14px;font-size:24px;color:#666;
  box-shadow:inset 0 1px 3px rgba(0,0,0,.12)}

.nav{left:104px;top:182px;width:988px;height:76px;border-radius:6px;
  background:linear-gradient(#3a8fd4,#1b6cb4);display:flex;box-shadow:0 3px 6px rgba(0,0,0,.25);overflow:hidden}
.nav a{display:flex;align-items:center;justify-content:center;color:var(--white);font-size:24px;text-decoration:none;
  border-right:2px solid #175f9f}
.nav a.active{background:linear-gradient(#6fb6ec,#4a9de0);color:#0b3a62}
.nav a:last-child{border-right:none}

.hero-art{left:480px;top:300px;width:580px;height:430px;
  background:radial-gradient(ellipse 45% 40% at 82% 42%,#151515 0%,#2a2a2a 60%,rgba(255,255,255,0) 100%),
             radial-gradient(ellipse 50% 42% at 35% 40%,#3f7fb6 0%,#6ea6d3 55%,rgba(255,255,255,0) 100%)}
.hero-title{left:126px;top:452px;color:var(--heading);white-space:nowrap}
.hero-title .big{font-size:48px;line-height:56px}
.hero-title .small{font-size:36px;line-height:46px}
.dots{left:128px;top:638px;display:flex;gap:6px}
.dots span{width:30px;height:30px;border-radius:50%;border:3px solid #7fb4d9;background:#eef6fc}
.dots span.on{background:#1d5d95}

.panel{left:106px;top:740px;width:992px;height:732px;border:2px solid var(--panel-border);border-radius:8px;
  background:var(--white);box-shadow:0 10px 24px rgba(0,0,0,.18)}
.feature{top:762px;width:302px;height:700px}
.feature-head{height:84px;border-radius:4px;background:linear-gradient(#5fb0ea,#2d80c8);color:var(--white);
  font-size:28px;font-weight:600;display:flex;align-items:center;justify-content:center;box-shadow:0 3px 5px rgba(0,0,0,.2)}
.feature-photo{margin:16px 6px 0;height:204px;border:3px solid #5ba3dd;border-radius:4px}
.feature-copy{margin:22px 6px 0;font-size:23px;line-height:32.7px;color:#2a3440}
.feature-copy span{display:block;text-align:justify;text-align-last:justify;white-space:nowrap}
.more{display:inline-flex;align-items:center;justify-content:center;width:82px;height:48px;border-radius:5px;
  background:linear-gradient(#74aedc,#2c6ea6);color:var(--white);font-size:20px;font-weight:600;box-shadow:0 2px 4px rgba(0,0,0,.3)}
.feature .more{position:absolute;top:638px;left:2px}

.welcome{left:122px;top:1500px;width:968px}
.welcome h1{font-size:32px;font-weight:400;color:var(--heading);margin-bottom:8px;line-height:42px}
.welcome p{font-size:24px;line-height:34px;text-align:justify}
.checks{list-style:none;margin:30px 0 32px 28px}
.checks li{font-size:24px;line-height:33px;display:flex;align-items:center;gap:12px}
.welcome p + p{margin-top:34px}

.footer{left:0;top:2044px;width:1200px;height:364px;background:var(--footer);color:#e6eef5}
.fcol{top:44px;font-size:18px;line-height:28px;white-space:nowrap}
.fcol h2{font-size:28px;font-weight:400;color:var(--white);margin-bottom:10px;line-height:34px}
.divider{top:48px;height:214px;border-left:4px dotted var(--divider)}
.social{margin-top:4px}
.social li{list-style:none;display:flex;align-items:center;gap:16px;height:41px}
.social .chip{width:30px;height:30px;border-radius:4px;background:#3b78b8;margin-left:40px}
.link{color:var(--link);font-weight:600}
.footer .more{margin-top:12px}
.copyright{left:0;top:2362px;width:1200px;text-align:center;font-size:18px;color:var(--link);text-decoration:underline}
</style>
</head>
<body>

<div class="abs brand">
  <div class="brand-mark"></div>
  <div class="brand-name">Harborline Coverage<br>Partners</div>
</div>

<div class="abs search">
  <span>Search here</span>
  <svg width="30" height="30" viewBox="0 0 30 30"><circle cx="17" cy="12" r="8" fill="none" stroke="#555" stroke-width="3"/><line x1="11" y1="18" x2="4" y2="26" stroke="#555" stroke-width="4" stroke-linecap="round"/></svg>
</div>

<nav class="abs nav">
  <a class="active" style="width:154px">Home</a>
  <a style="width:184px">About us</a>
  <a style="width:208px">Products</a>
  <a style="width:226px">Services</a>
  <a style="width:216px">Contact Us</a>
</nav>

<div class="abs hero-art" role="img" aria-label="World map with silhouettes of three businessmen"></div>
<div class="abs hero-title">
  <div class="big">Harborline Coverage</div>
  <div class="small">that makes your business<br>ahead among others.</div>
</div>
<div class="abs dots"><span class="on"></span><span></span><span></span></div>

<div class="abs panel"></div>

<section class="abs feature" style="left:126px">
  <div class="feature-head">Issue Reporting</div>
  <div class="feature-photo" role="img" aria-label="Advisors meeting with a couple at a desk" style="background:linear-gradient(135deg,#d9cbb8,#a88a6e 50%,#5d7ea8)"></div>
  <p class="feature-copy"><span>We are a boutique</span><span>financial services firm</span><span>specializing in solutions</span><span>that financial services</span><span>professionals can</span><span>integrate into</span><span>comprehensive wealth</span><span>preservation strategies</span><span>for their clients.</span></p>
  <span class="more">More</span>
</section>
<section class="abs feature" style="left:450px">
  <div class="feature-head">Strategic Plan</div>
  <div class="feature-photo" role="img" aria-label="Clasped hands of a businessman" style="background:linear-gradient(135deg,#6a7a8a,#caa088 50%,#2e3a48)"></div>
  <p class="feature-copy"><span>We are a boutique</span><span>financial services firm</span><span>specializing in solutions</span><span>that financial services</span><span>professionals can</span><span>integrate into</span><span>comprehensive wealth</span><span>preservation strategies</span><span>for their clients.</span></p>
  <span class="more">More</span>
</section>
<section class="abs feature" style="left:774px">
  <div class="feature-head">Resolving Issues</div>
  <div class="feature-photo" role="img" aria-label="Business handshake" style="background:linear-gradient(135deg,#bcd6ee,#c99a7c 50%,#1d2838)"></div>
  <p class="feature-copy"><span>We are a boutique</span><span>financial services firm</span><span>specializing in solutions</span><span>that financial services</span><span>professionals can</span><span>integrate into</span><span>comprehensive wealth</span><span>preservation strategies</span><span>for their clients.</span></p>
  <span class="more">More</span>
</section>

<section class="abs welcome">
  <h1>Welcome to our site</h1>
  <p>At Harborline Coverage Partners, protecting your clients’ families, their businesses, and their lifestyles are at the forefront of all we do.</p>
  <ul class="checks">
    <li><svg width="26" height="24" viewBox="0 0 26 24"><path d="M2 13 L9 20 L24 3" fill="none" stroke="#2a78c2" stroke-width="5" stroke-linecap="round" stroke-linejoin="round"/></svg>Unsurpassed service, support, and underwriting</li>
    <li><svg width="26" height="24" viewBox="0 0 26 24"><path d="M2 13 L9 20 L24 3" fill="none" stroke="#2a78c2" stroke-width="5" stroke-linecap="round" stroke-linejoin="round"/></svg>Licensed to conduct business nationally</li>
    <li><svg width="26" height="24" viewBox="0 0 26 24"><path d="M2 13 L9 20 L24 3" fill="none" stroke="#2a78c2" stroke-width="5" stroke-linecap="round" stroke-linejoin="round"/></svg>Advising businesses and families for over 50 years</li>
    <li><svg width="26" height="24" viewBox="0 0 26 24"><path d="M2 13 L9 20 L24 3" fill="none" stroke="#2a78c2" stroke-width="5" stroke-linecap="round" stroke-linejoin="round"/></svg>Independent, objective, and resourceful</li>
  </ul>
  <p>There are many advantages to working with Harborline Coverage Partners. We offer the service and attention of a boutique agency, while leveraging the strength of preeminent American and offshore life insurance companies.</p>
  <p>In addition, since we are privately owned we base our actions and recommendations on what is best for our clients without regard to stockholder profit or share price.</p>
</section>

<footer class="abs footer">
  <div class="abs fcol" style="left:108px;width:232px">
    <h2>Contacts</h2>
    18/4b, Pier Lane,<br>Bayview, OR<br>Email : hi@hcp.example<br>Phone : 00-0555-0182/<br>&nbsp;&nbsp;&nbsp;&nbsp;&nbsp;&nbsp;&nbsp;&nbsp;&nbsp;&nbsp;&nbsp;0555-0190<br>Fax : 800-0555-0147/<br>&nbsp;&nbsp;&nbsp;&nbsp;&nbsp;&nbsp;&nbsp;&nbsp;0555-0163
  </div>
  <div class="abs divider" style="left:344px"></div>
  <div class="abs fcol" style="left:364px;width:230px">
    <h2>Social Media</h2>
    Follow Us :
    <ul class="social">
      <li><span class="chip"></span>Facenote</li>
      <li><span class="chip" style="background:#b23a48"></span>Pinboardly</li>
      <li><span class="chip" style="background:#2c5f94"></span>Linkwork</li>
      <li><span class="chip" style="background:#3a9a9a"></span>Circlet</li>
    </ul>
  </div>
  <div class="abs divider" style="left:602px"></div>
  <div class="abs fcol" style="left:622px;width:220px">
    <h2>Blog</h2>
    <span class="link">Blog Title goes here</span><br>Dt: 21-Aug-2012<br>Description goes here.<br>Put something about<br>your topic.<br>
    <span class="more">More</span>
  </div>
  <div class="abs divider" style="left:852px"></div>
  <div class="abs fcol" style="left:868px;width:240px">
    <h2>Our Clients</h2>
    Our renowned clients<br>are;<br><span class="link">ABC Corporation</span><br><span class="link">XYZ Corporation</span><br><span class="link">Techno HighCity Ltd.</span><br>
    <span class="more">More</span>
  </div>
</footer>
<div class="abs copyright">Copyright @ 2012, HarborlineCoveragePartners</div>

</body>
</html>
```